Business card for psychiatrist

Business card design project for a psychiatristWe would like to have the impression of 1. We (patient and the doctor) are working together.2. Light the way so that patients can see where they are going and what their goals are.3. One side of the business card will have the letter "TFP" which stands for Thornvale Family Psychiatry.4. The other side of the business card will have the address, phone number, name of the psychiatrist, website, etc.5. A logo could go into either side of the business card. Let's see what looks better.
Business card design project for a psychiatrist
We would like to have the impression of
1. We (patient and the doctor) are working together.
2. Light the way so that patients can see where they are going and what their goals are.
3. One side of the business card will have the letter "TFP" which stands for Thornvale Family Psychiatry.
4. The other side of the business card will have the address, phone number, name of the psychiatrist, website, etc.
5. A logo could go into either side of the business card. Let's see what looks better.
Colors
Designer to choose colors to be used in the design.
Look and feel
Each slider illustrates characteristics of the customer's brand and the style your logo design should communicate.

```html
<!DOCTYPE html>
<html lang="en">
<head>
<meta charset="utf-8">
<title>Thornvale Family Psychiatry – Business Card</title>
<link rel="stylesheet" href="https://fonts.googleapis.com/css2?family=Cinzel:wght@500&family=Open+Sans:wght@400&display=swap">
<style>
  :root {
    --backdrop: #5b5b5b;
    --card-light: #f4f4f4;
    --brand-blue: #29a8df;
    --ink: #2b2b2b;
    --white: #ffffff;
  }
  * { margin: 0; padding: 0; box-sizing: border-box; }
  html, body { width: 1200px; height: 900px; overflow: hidden; }
  body {
    background: var(--backdrop);
    position: relative;
    font-family: "Open Sans", Arial, sans-serif;
  }
  .card {
    position: absolute;
    top: 200px;
    width: 310px;
    height: 502px;
    box-shadow: 3px 4px 6px rgba(0,0,0,0.35);
  }
  .card--front {
    left: 253px;
    background: var(--card-light);
    border-radius: 62px 0 62px 0;
  }
  .card--back {
    left: 627px;
    background: var(--brand-blue);
    border-radius: 0 62px 0 62px;
  }
  .brand {
    position: absolute;
    left: 0; right: 0;
    text-align: center;
    font-family: "Open Sans", Arial, sans-serif;
    font-weight: 400;
  }
  .brand__dot {
    display: block;
    margin: 0 auto 14px;
    width: 34px; height: 34px;
    border-radius: 50%;
  }
  .brand__name {
    display: block;
    font-size: 33px;
    letter-spacing: 1px;
    line-height: 1;
  }
  .brand__tagline {
    display: block;
    font-size: 11px;
    letter-spacing: 3.6px;
    margin-top: 6px;
  }
  .card--front .brand { top: 90px; color: var(--brand-blue); }
  .card--front .brand__dot { background: var(--brand-blue); }
  .card--back .brand { top: 190px; color: var(--white); }
  .card--back .brand__dot { background: var(--white); }

  .contact {
    position: absolute;
    left: 32px;
    top: 302px;
    color: var(--ink);
  }
  .contact__name {
    font-family: "Cinzel", Georgia, serif;
    font-weight: 500;
    color: var(--brand-blue);
    font-size: 19px;
    letter-spacing: 0.5px;
    line-height: 1;
  }
  .contact__role { font-size: 14px; margin-top: 4px; }
  .contact__list { list-style: none; margin-top: 6px; }
  .contact__item {
    font-size: 14px;
    line-height: 18.5px;
    display: flex;
    align-items: center;
  }
  .contact__icon { width: 12px; height: 12px; margin-right: 4px; fill: var(--brand-blue); }
  .contact__address { font-size: 14px; line-height: 18.5px; margin-top: 8px; font-style: normal; }
</style>
</head>
<body>
  <section class="card card--front">
    <div class="brand">
      <span class="brand__dot"></span>
      <span class="brand__name">THORNVALE</span>
      <span class="brand__tagline">FAMILY PSYCHIATRY</span>
    </div>
    <div class="contact">
      <p class="contact__name">DANIEL MARSH</p>
      <p class="contact__role">Managing Director</p>
      <ul class="contact__list">
        <li class="contact__item">
          <svg class="contact__icon" viewBox="0 0 12 12"><path d="M1 4c0-2 2-3 5-3s5 1 5 3l-2 1-1-1H4L3 5zM2 6h8l1 5H1z"/></svg>044-555 210 387
        </li>
        <li class="contact__item">
          <svg class="contact__icon" viewBox="0 0 12 12"><path d="M3 0h6v12H3zM4 1.5v8h4v-8z"/></svg>044-555 210 387
        </li>
        <li class="contact__item">
          <svg class="contact__icon" viewBox="0 0 12 12"><path d="M0 2.5h12v7H0zM1 3.2l5 3.6 5-3.6z" fill-rule="evenodd"/></svg>info@thornvalefp.com
        </li>
        <li class="contact__item">
          <svg class="contact__icon" viewBox="0 0 12 12"><circle cx="6" cy="6" r="5.5"/></svg>www.thornvalefp.com
        </li>
      </ul>
      <address class="contact__address">48 Harrow Lane, Suite 210<br>Maple County, 204517.</address>
    </div>
  </section>

  <section class="card card--back">
    <div class="brand">
      <span class="brand__dot"></span>
      <span class="brand__name">THORNVALE</span>
      <span class="brand__tagline">FAMILY PSYCHIATRY</span>
    </div>
  </section>
</body>
</html>
```